Group Medical Practice needs stationery, business cards etc. designed

We need stationery designed for a multisite practice that offers primary medical, dental and behavioral healthcare. We would like a design that is consistent for letterhead, business cards, Microsoft Outlook stationery etc. We have attached our new logo design.

Business

```html
<!DOCTYPE html>
<html lang="en">
<head>
<meta charset="utf-8">
<title>Cedar Ridge Health Services – Stationery Set</title>
<link rel="stylesheet" href="https://fonts.googleapis.com/css2?family=Cinzel:wght@600&display=swap">
<style>
  :root {
    --canvas: #ffffff;
    --frame: #3a3a3a;
    --paper: #ffffff;
    --paper-edge: #6b6b6b;
    --brand-green: #8dc63f;
    --tint-green: #e2efd4;
    --brand-blue: #1a7bc0;
    --disc-edge: #333333;
  }
  html, body {
    margin: 0;
    padding: 0;
    width: 1200px;
    height: 1001px;
    overflow: hidden;
    background: var(--canvas);
  }
  .stationery-board {
    display: block;
    width: 1200px;
    height: 1001px;
  }
  .board-frame { fill: var(--canvas); stroke: var(--frame); stroke-width: 1.5; }
  .paper { fill: var(--paper); stroke: var(--paper-edge); stroke-width: 1; }
  .accent-band { fill: var(--brand-green); }
  .tinted-back { fill: var(--tint-green); stroke: var(--paper-edge); stroke-width: 1; }
  .disc { fill: var(--tint-green); stroke: var(--disc-edge); stroke-width: 1.2; }
  .disc-hole { fill: var(--paper); stroke: var(--disc-edge); stroke-width: 2.5; }
  .brand-name,
  .brand-sub {
    font-family: "Cinzel", serif;
    font-weight: 600;
    fill: var(--brand-blue);
    text-anchor: middle;
  }
  .brand-name { font-size: 16px; letter-spacing: 0.5px; }
  .brand-sub { font-size: 8.5px; letter-spacing: 1px; }
  .brand-name.small { font-size: 13px; }
  .brand-sub.small { font-size: 7px; }
</style>
</head>
<body>
<svg class="stationery-board" viewBox="0 0 1200 1001" xmlns="http://www.w3.org/2000/svg">
  <rect class="board-frame" x="1" y="1" width="1198" height="999"/>

  <!-- Business card, front -->
  <g class="business-card-front">
    <rect class="paper" x="47" y="80" width="392" height="216"/>
    <polygon class="accent-band" points="439,100 439,296 100,296 418,277"/>
    <text class="brand-name" x="167" y="160">Cedar Ridge</text>
    <text class="brand-sub" x="167" y="172">Health Services</text>
  </g>

  <!-- Business card, back -->
  <rect class="tinted-back business-card-back" x="45" y="318" width="392" height="216"/>

  <!-- Disc label -->
  <g class="disc-label">
    <circle class="disc" cx="219" cy="739" r="132"/>
    <circle class="disc-hole" cx="219" cy="739" r="32"/>
    <text class="brand-name small" x="217" y="830">Cedar Ridge</text>
    <text class="brand-sub small" x="217" y="840">Health Services</text>
  </g>

  <!-- Large envelope -->
  <g class="envelope-large">
    <polygon class="accent-band" points="808,125 1157,125 1186,183 778,183"/>
    <rect class="paper" x="778" y="183" width="408" height="571"/>
    <polygon class="accent-band" points="1186,185 1186,754 878,754 1157,727"/>
    <text class="brand-name" x="885" y="265">Cedar Ridge</text>
    <text class="brand-sub" x="885" y="277">Health Services</text>
  </g>

  <!-- Letterhead -->
  <g class="letterhead">
    <rect class="paper" x="470" y="288" width="408" height="573"/>
    <polygon class="accent-band" points="878,300 878,861 475,861 849,833"/>
    <text class="brand-name" x="575" y="364">Cedar Ridge</text>
    <text class="brand-sub" x="575" y="376">Health Services</text>
  </g>

  <!-- DL envelope -->
  <g class="envelope-dl">
    <polygon class="accent-band" points="585,443 975,443 992,485 572,485"/>
    <rect class="paper" x="572" y="485" width="420" height="192"/>
    <polygon class="accent-band" points="992,487 992,677 650,677 971,658"/>
    <text class="brand-name" x="671" y="650">Cedar Ridge</text>
    <text class="brand-sub" x="671" y="662">Health Services</text>
  </g>
</svg>
</body>
</html>
```